Baby Girl Maud Birth Announcement for Dec 1st 2020

Using an existing photo from an artist, build a 2 sided card with messaging and details on opposite side.

Style: fun, timeless, elegant, vibrant
Side 1:
Text "Welcome Maud".
Use file called FRONT BACKGROUND - Welcome Maud.
Consider 2 fonts, consider 2 colors of words. use provided image and monochromatic image of a heart
Side 2 content to be fit:
"Welcome to our little ray of light!"
"Maud Iris Jane Pelham"
Date of birth ---/--/----
Time of birth
Weight
Length
"Loving and Proud Parents : Clara Pelham - Ter Horst & Gregor Pelham"
Amazing and Wonderful God Parents : "Lehuanani Kekoa & Bastien De Wulf" + "Mira Chen Holloway & Dustin Holloway "

Target Market(s)

Family and friends.
International audience (european/asian/american).
Urban, up market,

Requirements
Must have
• Use file called FRONT BACKGROUND - Welcome Maud on the front
Nice to have
• Consider 2 fonts, consider 2 colors of words. use provided image and monochromatic image of a heart

```html
<!DOCTYPE html>
<html lang="en">
<head>
<meta charset="utf-8">
<title>Welcome Maud – Birth Announcement, Front</title>
<link rel="stylesheet" href="https://fonts.googleapis.com/css2?family=Great+Vibes&family=Playfair+Display:wght@700&display=swap">
<style>
  :root {
    --page-bg: #f1efea;
    --card-paper: #fcfbf8;
    --script-brown: #3a2a12;
    --gold-light: #e7b457;
    --gold-mid: #c98a2c;
    --gold-dark: #9a6318;
    --card-shadow: rgba(60, 55, 50, 0.35);
  }
  * { margin: 0; padding: 0; box-sizing: border-box; }
  html, body {
    width: 1200px;
    height: 1200px;
    overflow: hidden;
    background: var(--page-bg);
  }
  .canvas {
    position: relative;
    width: 1200px;
    height: 1200px;
  }
  .card-front {
    position: absolute;
    left: 50px;
    top: 244px;
    width: 1100px;
    height: 712px;
    background: var(--card-paper);
    box-shadow: 0 6px 18px var(--card-shadow);
    overflow: hidden;
  }
  .front-photo {
    position: absolute;
    inset: 0;
    background:
      radial-gradient(ellipse 18% 22% at 85% 44%, rgba(255, 252, 235, 0.95), rgba(255, 245, 200, 0) 100%),
      radial-gradient(ellipse 30% 30% at 78% 48%, rgba(240, 205, 110, 0.75), rgba(240, 205, 110, 0) 100%),
      radial-gradient(ellipse 12% 26% at 76% 64%, rgba(225, 225, 222, 0.9), rgba(225, 225, 222, 0) 100%),
      radial-gradient(ellipse 22% 24% at 10% 50%, rgba(90, 160, 205, 0.85), rgba(90, 160, 205, 0) 100%),
      radial-gradient(ellipse 30% 22% at 15% 32%, rgba(95, 110, 140, 0.65), rgba(95, 110, 140, 0) 100%),
      radial-gradient(ellipse 40% 26% at 45% 38%, rgba(120, 145, 80, 0.7), rgba(120, 145, 80, 0) 100%),
      radial-gradient(ellipse 22% 16% at 30% 72%, rgba(200, 185, 160, 0.6), rgba(200, 185, 160, 0) 100%),
      linear-gradient(180deg, var(--card-paper) 0%, var(--card-paper) 14%, rgba(236, 236, 230, 1) 55%, #f3f4f4 80%, var(--card-paper) 100%);
  }
  .front-photo::after {
    content: "";
    position: absolute;
    inset: 0;
    background: linear-gradient(180deg, rgba(252, 251, 248, 0.9) 0%, rgba(252, 251, 248, 0) 22%, rgba(252, 251, 248, 0) 78%, rgba(252, 251, 248, 0.85) 100%);
  }
  .greeting {
    position: absolute;
    left: 0;
    right: 0;
    top: 262px;
    text-align: center;
  }
  .greeting-welcome {
    display: block;
    font-family: "Great Vibes", cursive;
    font-size: 138px;
    line-height: 1;
    color: var(--script-brown);
    margin-left: -26px;
  }
  .greeting-name {
    position: absolute;
    left: 0;
    right: 0;
    top: 412px;
    text-align: center;
    font-family: "Playfair Display", serif;
    font-weight: 700;
    font-size: 176px;
    line-height: 1;
    letter-spacing: 2px;
    margin-left: -18px;
    background: linear-gradient(160deg, var(--gold-light) 0%, var(--gold-mid) 45%, var(--gold-dark) 70%, var(--gold-light) 100%);
    -webkit-background-clip: text;
    background-clip: text;
    color: transparent;
    filter: drop-shadow(2px 3px 2px rgba(70, 45, 10, 0.35));
  }
</style>
</head>
<body>
  <main class="canvas">
    <section class="card-front">
      <div class="front-photo" role="img" aria-label="Soft-focus artist photo of small toy figures in a snowy scene with a glittering unicorn-costumed figure, warm golden sunlight and blurred green and blue background"></div>
      <h1 class="greeting">
        <span class="greeting-welcome">Welcome</span>
      </h1>
      <p class="greeting-name">MAUD</p>
    </section>
  </main>
</body>
</html>
```